Brisk Yonder Podcast Pic

The pic I'll be using for my podcast.
On the design I need my name, Dana Pellham
The podcast name, Brisk Yonder
The picture and anything else you think would work(the lower part of the picture can be cut if needed. Please let me know if the image works or if you need a better quality.

the podcast is about moving forward after a tragedy and going on to accomplishing great things.

```html
<!DOCTYPE html>
<html lang="en">
<head>
<meta charset="UTF-8">
<title>Brisk Yonder with Dana Pellham</title>
<link rel="stylesheet" href="https://fonts.googleapis.com/css2?family=Montserrat:ital,wght@0,300;0,400;1,700&display=swap">
<style>
  :root {
    --sun-yellow: #ffc906;
    --royal-blue: #0052c2;
    --ice-text: #e4fbff;
    --glow-cyan: #c9f6ff;
    --portrait-dark: #2a211d;
    --portrait-mid: #8a6a52;
    --portrait-light: #e9c9ae;
  }
  html, body {
    margin: 0;
    padding: 0;
    overflow: hidden;
    background: var(--sun-yellow);
  }
  .cover {
    position: relative;
    width: 1200px;
    height: 1200px;
    overflow: hidden;
    background: var(--sun-yellow);
    font-family: "Montserrat", "Helvetica Neue", Arial, sans-serif;
  }
  .cover__arrow {
    position: absolute;
    inset: 0;
    width: 1200px;
    height: 1200px;
  }
  .cover__arrow polygon { fill: var(--royal-blue); }
  .title {
    position: absolute;
    top: 180px;
    left: 0;
    width: 1200px;
    margin: 0;
    text-align: center;
    color: var(--ice-text);
    font-size: 118px;
    line-height: 1;
    font-weight: 300;
    letter-spacing: 0.02em;
    white-space: nowrap;
  }
  .title__accent {
    font-weight: 700;
    font-style: italic;
    letter-spacing: 0.01em;
  }
  .host {
    position: absolute;
    top: 312px;
    left: 0;
    width: 1200px;
    margin: 0;
    text-align: center;
    color: var(--ice-text);
    font-size: 54px;
    line-height: 1;
    font-weight: 400;
    letter-spacing: 0.2em;
    white-space: nowrap;
  }
  .portrait {
    position: absolute;
    left: 175px;
    top: 600px;
    width: 860px;
    height: 640px;
    border-radius: 300px 300px 0 0;
    background:
      radial-gradient(ellipse 28% 30% at 50% 55%, var(--portrait-light) 0%, var(--portrait-mid) 70%, transparent 100%),
      linear-gradient(180deg, var(--portrait-dark) 0%, #3b2f28 45%, var(--portrait-dark) 100%);
    box-shadow: 0 0 28px 14px var(--glow-cyan);
  }
</style>
</head>
<body>
  <main class="cover">
    <svg class="cover__arrow" viewBox="0 0 1200 1200" aria-hidden="true">
      <polygon points="0,0 600,0 1200,366 0,1056"/>
    </svg>

    <h1 class="title">BRISK <span class="title__accent">YONDER</span></h1>
    <p class="host">WITH DANA PELLHAM</p>

    <div class="portrait" role="img" aria-label="Portrait photo of the host in a wide black hat and leather jacket, looking upward"></div>
  </main>
</body>
</html>
```